Safety Consultancy focusing on developing exceptional Safety Leaders

I need a full but simple, modern, catchy website to drive business - my focus is on helping organizations to understand the impact that leaders have on safety performance and how they build the processes to make that happen. I already have great branding (logos) built through PixelGuild and can provide all narrative to build out the pages

Target Market(s)

Focused internationally. Typical client has a fairly robust and mature safety culture yet lacks the focused effort to develop all levels of leadership in terms of managing safety. Exercising these competencies results in continued development of an organizations safety culture as well as improved safety performance

Industry/Entity Type

all

Coding

Coded - Design and coding required

Number of Pages Required

4 page

Font styles to use
Other font styles liked:
• to match my branding

Colors
0054AA
0677BA
7BADD7
CADEEF
E8F1F8

Requirements
Must have
• Must utilize my current branding, logo, etc. I want to have a page outlining clearly my vision - which I will add to my uploads as we move forward. I need to have a page listing my extensive and unique experience as well as successes
Nice to have
• Want to leave it up to designers - but needs to be simple and easily navigable - hope to have a resource page that I can update myself with safety resource info, reports, etc.

```html
<!DOCTYPE html>
<html lang="en">
<head>
<meta charset="utf-8">
<title>Halvorn Ventures International</title>
<link href="https://fonts.googleapis.com/css2?family=Poppins:wght@400;500;600;700&display=swap" rel="stylesheet">
<style>
:root{
  --brand:#2e2a8c;
  --brand-dark:#1c1755;
  --navy:#1a1650;
  --ink:#1d1d2b;
  --muted:#6b6b78;
  --soft:#f3f3f6;
  --white:#ffffff;
  --line:#d9d9e3;
}
*{box-sizing:border-box;margin:0;padding:0}
html,body{width:1200px;height:4380px;overflow:hidden}
body{font-family:'Poppins',sans-serif;color:var(--ink);background:var(--white);position:relative}
.abs{position:absolute}
.btn{position:absolute;display:flex;align-items:center;justify-content:center;background:var(--brand);color:var(--white);font-size:13px;font-weight:600;border-radius:22px}
.eyebrow{position:absolute;font-size:34px;font-weight:700;color:var(--brand)}
.subhead{position:absolute;font-size:27px;font-weight:500;line-height:1.42;padding-left:24px;border-left:9px solid var(--brand);color:var(--ink)}
.body-copy{position:absolute;font-size:15px;line-height:1.45;color:var(--muted)}
.photo{position:absolute}

/* header */
.topbar{left:365px;top:0;width:835px;height:46px;background:var(--brand);clip-path:polygon(0 0,100% 0,100% 100%,30px 100%);display:flex;align-items:center;color:#dcdcf2;font-size:12px}
.topbar .item{display:flex;align-items:center;gap:7px}
.brand{left:58px;top:34px;display:flex;align-items:center;gap:12px}
.brand .dot{width:46px;height:46px;border-radius:50%;background:var(--brand)}
.brand .name{font-size:22px;font-weight:700;color:var(--brand);line-height:1.1}
.nav{left:394px;top:72px;display:flex;gap:24px;font-size:13px;font-weight:500;color:#8b8b98}
.nav .active{color:var(--brand)}
.nav-marker{left:409px;top:110px;width:11px;height:11px;border-radius:50%;background:var(--brand)}

/* hero */
.hero{left:0;top:116px;width:1200px;height:640px;background:linear-gradient(100deg,#1b1a4a 0%,#2a2770 60%,#2e2a80 100%)}
.hero h1{position:absolute;left:111px;top:170px;font-size:52px;line-height:1.38;color:var(--white);font-weight:600;letter-spacing:.5px}
.hero p{position:absolute;left:111px;top:320px;font-size:15px;color:#e4e4f4;line-height:1.45;width:340px}

/* stats */
.stat{position:absolute;top:1479px;width:156px;height:156px;background:var(--white);text-align:center;box-shadow:0 6px 20px rgba(30,30,80,.06)}
.stat b{display:block;margin-top:34px;font-size:51px;font-weight:600;color:var(--brand);line-height:1.1}
.stat span{display:block;margin-top:8px;font-size:15px;color:var(--ink)}
.stat i{position:absolute;left:26px;right:26px;bottom:0;height:6px;border-radius:6px 6px 0 0;background:var(--brand)}

/* services */
.service-line{position:absolute;top:1964px;height:3px;background:var(--brand)}
.service-dot{position:absolute;top:1956px;width:19px;height:19px;border-radius:50%;background:var(--brand);border:3px solid var(--white)}
.service-label{position:absolute;top:2308px;width:313px;text-align:center;font-size:18px;font-weight:600}

/* stories */
.story{position:absolute;overflow:hidden;border-radius:3px}
.story .band{position:absolute;left:0;right:0;bottom:0;height:102px;background:rgba(46,42,140,.92);color:var(--white);padding:24px 24px}
.story .band b{font-size:22px;font-weight:600;display:block}
.story .band small{font-size:13px;color:#d6d6ee}
.story .play{position:absolute;width:82px;height:82px;border-radius:50%;background:rgba(46,42,140,.85);display:flex;align-items:center;justify-content:center}

/* resources */
.res-img{position:absolute;top:3130px;width:313px;height:192px;border-radius:3px}
.tag{position:absolute;top:3285px;padding:4px 20px;border-radius:16px;background:var(--white);color:var(--brand);font-size:13px;font-weight:600}
.res-title{position:absolute;top:3350px;width:330px;font-size:18px;font-weight:600;line-height:1.45}
.res-link{position:absolute;top:3430px;font-size:13px;font-weight:600;color:var(--brand);display:flex;align-items:center;gap:12px}

/* footer */
.footer{left:0;top:3600px;width:1200px;height:780px;background:var(--navy);color:var(--white)}
.contact-line{position:absolute;display:flex;align-items:center;gap:18px;font-size:12px;color:#d8d8ea}
.icon-circ{width:30px;height:30px;border-radius:50%;background:var(--brand);display:flex;align-items:center;justify-content:center;flex:none}
.label{position:absolute;font-size:14px;font-weight:600;letter-spacing:.5px}
.field{position:absolute;background:var(--white);border-radius:4px;color:#8a8a96;font-size:14px;padding:15px 20px}
.col-head{position:absolute;top:4105px;font-size:13px;color:#c8c8de}
.col{position:absolute;top:4150px;font-size:12px;line-height:30px;color:#e4e4f2}
</style>
</head>
<body>

<!-- Header -->
<div class="abs topbar">
  <div class="item" style="margin-left:60px">
    <svg width="13" height="13" viewBox="0 0 24 24" fill="none" stroke="#fff" stroke-width="2"><path d="M22 16.9v3a2 2 0 0 1-2.2 2A19.8 19.8 0 0 1 2.1 4.2 2 2 0 0 1 4.1 2h3a2 2 0 0 1 2 1.7c.1.9.4 1.8.7 2.7a2 2 0 0 1-.5 2.1L8 9.8a16 16 0 0 0 6 6l1.3-1.3a2 2 0 0 1 2.1-.4c.9.3 1.8.6 2.7.7a2 2 0 0 1 1.7 2z"/></svg>
    1-555-014-2290
  </div>
  <div class="item" style="margin-left:150px">
    <svg width="14" height="12" viewBox="0 0 24 20" fill="none" stroke="#fff" stroke-width="2"><rect x="1" y="1" width="22" height="18" rx="2"/><path d="M1 3l11 8 11-8"/></svg>
    hello@halvorn.example
  </div>
  <div class="item" style="margin-left:160px;gap:8px">
    <span style="width:10px;height:10px;border-radius:50%;background:#fff" aria-label="Social link"></span>
    <span style="width:10px;height:10px;border-radius:50%;background:#fff" aria-label="Social link"></span>
    <span style="width:10px;height:10px;background:#fff" aria-label="Social link"></span>
  </div>
</div>
<div class="abs brand">
  <div class="dot"></div>
  <div class="name">Halvorn<br><span style="font-size:15px">Ventures International</span></div>
</div>
<nav class="abs nav">
  <span class="active">Home</span><span>About Us</span><span>Our Vision</span><span>Our Services</span><span>Success Stories</span><span>Resources</span>
</nav>
<div class="abs nav-marker"></div>
<div class="btn" style="left:981px;top:62px;width:128px;height:40px">Contact Us</div>

<!-- Hero -->
<section class="abs hero">
  <h1>Empowering Leaders,<br>Enhancing Safety</h1>
  <p>Transforming safety performance through leadership excellence</p>
  <div class="btn" style="left:111px;top:400px;width:133px;height:37px">Learn More</div>
  <svg class="abs" style="left:660px;top:0" width="460" height="590" viewBox="0 0 460 590">
    <circle cx="300" cy="145" r="62" fill="none" stroke="#fff" stroke-width="8"/>
    <circle cx="222" cy="353" r="212" fill="#fff"/>
    <circle cx="222" cy="353" r="203" fill="#3b36a8"/>
    <circle cx="368" cy="493" r="60" fill="#2e2a8c" stroke="#fff" stroke-width="4"/>
  </svg>
  <div class="photo" role="img" aria-label="Portrait of the consultant in a navy suit" style="left:710px;top:40px;width:340px;height:470px;border-radius:170px 170px 200px 200px;background:linear-gradient(180deg,#5a5bb0 0%,#24306e 100%)"></div>
  <svg class="abs" style="left:0;top:570px" width="1200" height="75" viewBox="0 0 1200 75" preserveAspectRatio="none">
    <path d="M0 30 C200 70 420 -10 700 30 S1050 30 1200 10 L1200 75 L0 75Z" fill="#fff"/>
    <path d="M0 24 C200 64 420 -16 700 24 S1050 24 1200 4" fill="none" stroke="#fff" stroke-width="3"/>
  </svg>
</section>

<!-- About -->
<svg class="abs" style="left:120px;top:810px" width="460" height="470" viewBox="0 0 460 470">
  <path d="M290 20 A200 200 0 0 1 390 380" fill="none" stroke="#2e2a8c" stroke-width="3"/>
  <path d="M305 5 A218 218 0 0 1 445 240" fill="none" stroke="#2e2a8c" stroke-width="3"/>
</svg>
<div class="photo" role="img" aria-label="Team meeting with a presenter in an office" style="left:130px;top:848px;width:404px;height:384px;border-radius:50%;background:linear-gradient(135deg,#e4e6ee,#a7aabc)"></div>
<div class="abs" style="left:140px;top:1045px;width:210px;height:210px;border-radius:50%;border:3px solid #2e2a8c"></div>
<div class="photo" role="img" aria-label="Colleagues reviewing work at a desk" style="left:160px;top:1065px;width:170px;height:170px;border-radius:50%;background:linear-gradient(135deg,#cfd1dc,#8b8ea2);border:5px solid #fff"></div>
<div class="eyebrow" style="left:620px;top:855px">About Us</div>
<div class="subhead" style="left:620px;top:911px">Expertise &amp; Passion for Safety<br>Leadership</div>
<div class="body-copy" style="left:620px;top:995px;width:450px">Our consultancy was founded with the mission to enhance organizational safety performance through effective leadership. We believe that strong leadership is the key to fostering a robust safety culture and achieving continuous improvement in safety performance. Our approach is internationally focused, partnering with organizations that have a mature safety culture but seek to develop their leadership capabilities further.</div>
<div class="btn" style="left:620px;top:1204px;width:134px;height:39px">Read More</div>

<!-- Vision -->
<section class="abs" style="left:0;top:1334px;width:1200px;height:434px;background:var(--soft)"></section>
<div class="eyebrow" style="left:113px;top:1400px">Our Vision</div>
<div class="subhead" style="left:113px;top:1455px">Leadership Excellence for<br>Superior Safety Performance</div>
<div class="body-copy" style="left:113px;top:1540px;width:450px">We envision a world where every organization excels in safety through the power of effective leadership.Our approach focuses on developing leadership competencies that drive safety performance and culture improvement.</div>
<div class="btn" style="left:113px;top:1662px;width:133px;height:39px">Read More</div>
<div class="stat" style="left:588px"><b>25+</b><span>Years</span><i></i></div>
<div class="stat" style="left:760px"><b>35K+</b><span>Customer</span><i></i></div>
<div class="stat" style="left:932px"><b>34k+</b><span>Develop Strategy</span><i></i></div>

<!-- Services -->
<div class="eyebrow" style="left:122px;top:1835px">Our Services</div>
<div class="subhead" style="left:113px;top:1885px;font-size:27px;border-left-width:11px;padding-left:14px;line-height:1.2">Tailored Solutions for Enhanced Safety Leadership</div>
<div class="service-line" style="left:112px;width:140px"></div>
<div class="service-dot" style="left:258px"></div>
<div class="service-dot" style="left:590px"></div>
<div class="service-dot" style="left:921px"></div>
<div class="photo" role="img" aria-label="Business team celebrating with raised fists" style="left:112px;top:1966px;width:313px;height:312px;background:linear-gradient(180deg,#dfe4ee,#5c6684)"></div>
<div class="photo" role="img" aria-label="Worker in high-visibility vest holding a yellow hard hat" style="left:444px;top:1966px;width:313px;height:312px;background:linear-gradient(160deg,#3c3a3a,#8a7a40 55%,#e3c12a)"></div>
<div class="photo" role="img" aria-label="Facilitator presenting at a board with sticky notes" style="left:775px;top:1966px;width:313px;height:312px;background:linear-gradient(180deg,#2c3036,#b8b0a6)"></div>
<div class="service-label" style="left:112px">Leadership Training Programs</div>
<div class="service-label" style="left:444px">Safety Culture Assessment</div>
<div class="service-label" style="left:775px">Customized Safety Processes</div>

<!-- Success Stories -->
<section class="abs" style="left:0;top:2400px;width:1200px;height:541px;background:var(--soft)"></section>
<div class="eyebrow" style="left:113px;top:2487px">Success Stories</div>
<div class="subhead" style="left:113px;top:2542px">Proven Results in<br>Safety Leadership</div>
<div class="body-copy" style="left:113px;top:2628px;width:300px">Lorem Ipsum is simply dummy text of the printing and typesetting industry. Lorem Ipsum has been the industry's standard dummy text ever since the 1500s, when an unknown printer took a galley of type and scrambled it to make a type specimen book.</div>
<div class="btn" style="left:113px;top:2816px;width:133px;height:39px">View More</div>
<div class="story" style="left:445px;top:2467px;width:312px;height:367px">
  <div role="img" aria-label="Businessman in a suit at a meeting" style="position:absolute;inset:0;background:linear-gradient(180deg,#c8ccd6,#4a5370)"></div>
  <div class="play" style="left:115px;top:90px"><svg width="14" height="16" viewBox="0 0 14 16"><path d="M0 0L14 8L0 16Z" fill="#fff"/></svg></div>
  <div class="band"><b>Remittance</b><small>Digital Banking Business</small>
    <svg style="position:absolute;right:24px;top:48px" width="36" height="10" viewBox="0 0 36 10"><path d="M0 5H34M29 1L34 5L29 9" fill="none" stroke="#fff" stroke-width="1.5"/></svg></div>
</div>
<div class="story" style="left:775px;top:2511px;width:311px;height:362px">
  <div role="img" aria-label="Team collaborating around a whiteboard" style="position:absolute;inset:0;background:linear-gradient(160deg,#d9d6d0,#6e7590)"></div>
  <div class="play" style="left:115px;top:90px"><svg width="14" height="16" viewBox="0 0 14 16"><path d="M0 0L14 8L0 16Z" fill="#fff"/></svg></div>
  <div class="band"><b>Digital Marketing</b><small>Services Provider For&nbsp; Business</small>
    <svg style="position:absolute;right:24px;top:48px" width="36" height="10" viewBox="0 0 36 10"><path d="M0 5H34M29 1L34 5L29 9" fill="none" stroke="#fff" stroke-width="1.5"/></svg></div>
</div>

<!-- Resources -->
<div class="eyebrow" style="left:113px;top:3010px">Resources</div>
<div class="subhead" style="left:113px;top:3060px;border-left-width:11px;padding-left:14px;line-height:1.2">Your Source for Safety Leadership Information</div>
<div class="abs" style="left:916px;top:3046px;width:170px;height:38px;border:1.5px solid var(--brand);border-radius:20px;color:var(--brand);font-size:14px;display:flex;align-items:center;justify-content:center;gap:10px">Safety Reports
  <svg width="10" height="6" viewBox="0 0 10 6"><path d="M1 1L5 5L9 1" fill="none" stroke="#2e2a8c" stroke-width="1.5"/></svg></div>
<div class="res-img" role="img" aria-label="Speaker addressing a seated audience" style="left:112px;background:linear-gradient(160deg,#e6e8ee,#7c8196)"></div>
<div class="res-img" role="img" aria-label="Workshop group around conference tables" style="left:443px;background:linear-gradient(160deg,#e2e3e8,#8a8fa3)"></div>
<div class="res-img" role="img" aria-label="Colleagues working together at laptops" style="left:774px;background:linear-gradient(160deg,#ebe9e4,#8e90a0)"></div>
<div class="tag" style="left:125px">Upcoming</div>
<div class="tag" style="left:455px">Latest Report</div>
<div class="tag" style="left:786px">Old Report</div>
<div class="res-title" style="left:113px">Your Source for Safety Leadership Information</div>
<div class="res-title" style="left:443px">Your Source for Safety Leadership Information</div>
<div class="res-title" style="left:774px">Your Source for Safety Leadership Information</div>
<div class="res-link" style="left:113px">Read more <svg width="10" height="10" viewBox="0 0 10 10"><path d="M1 9L9 1M3 1H9V7" fill="none" stroke="#2e2a8c" stroke-width="1.5"/></svg></div>
<div class="res-link" style="left:443px">Read more <svg width="10" height="10" viewBox="0 0 10 10"><path d="M1 9L9 1M3 1H9V7" fill="none" stroke="#2e2a8c" stroke-width="1.5"/></svg></div>
<div class="res-link" style="left:774px">Read more <svg width="10" height="10" viewBox="0 0 10 10"><path d="M1 9L9 1M3 1H9V7" fill="none" stroke="#2e2a8c" stroke-width="1.5"/></svg></div>
<div class="btn" style="left:533px;top:3500px;width:134px;height:39px">View More</div>

<!-- Footer -->
<svg class="abs" style="left:0;top:3585px" width="1200" height="40" viewBox="0 0 1200 40" preserveAspectRatio="none">
  <path d="M0 30 C250 0 500 35 750 18 S1050 5 1200 8" fill="none" stroke="#1a1650" stroke-width="3"/>
</svg>
<section class="abs footer">
  <svg class="abs" style="left:0;top:-10px" width="1200" height="40" viewBox="0 0 1200 40" preserveAspectRatio="none">
    <path d="M0 0 L1200 0 L1200 12 C1050 8 900 30 700 22 S250 5 0 30Z" fill="#fff"/>
  </svg>
  <div class="subhead" style="left:113px;top:92px;color:#fff;border-left-color:var(--brand)">Ready to Transform Your<br>Safety Performance?</div>
  <div class="abs" style="left:113px;top:180px;width:430px;font-size:13px;line-height:2;color:#d8d8ea">We'd love to hear from you! Whether you have a question about our services, need assistance, or want to give feedback, our team is ready to assist you</div>
  <div class="contact-line" style="left:113px;top:283px"><span class="icon-circ"><svg width="12" height="12" viewBox="0 0 24 24" fill="none" stroke="#fff" stroke-width="2"><path d="M22 16.9v3a2 2 0 0 1-2.2 2A19.8 19.8 0 0 1 2.1 4.2 2 2 0 0 1 4.1 2h3a2 2 0 0 1 2 1.7c.1.9.4 1.8.7 2.7a2 2 0 0 1-.5 2.1L8 9.8a16 16 0 0 0 6 6l1.3-1.3a2 2 0 0 1 2.1-.4c.9.3 1.8.6 2.7.7a2 2 0 0 1 1.7 2z"/></svg></span>1-555-014-2290</div>
  <div class="contact-line" style="left:113px;top:335px"><span class="icon-circ"><svg width="13" height="11" viewBox="0 0 24 20" fill="none" stroke="#fff" stroke-width="2"><rect x="1" y="1" width="22" height="18" rx="2"/><path d="M1 3l11 8 11-8"/></svg></span>hello@halvorn.example</div>
  <div class="contact-line" style="left:113px;top:387px;line-height:1.4"><span class="icon-circ"><svg width="11" height="14" viewBox="0 0 20 26" fill="none" stroke="#fff" stroke-width="2"><path d="M10 25S2 15 2 9a8 8 0 0 1 16 0c0 6-8 16-8 16z"/><circle cx="10" cy="9" r="3"/></svg></span>2140 Larch Ave. Cedar Bay,<br>British Columbia, Canada. V0X 2B7</div>

  <div class="abs" style="left:602px;top:92px;font-size:26px;font-weight:500">Get in Touch</div>
  <div class="label" style="left:602px;top:158px">NAME</div>
  <div class="label" style="left:852px;top:158px">EMAIL</div>
  <div class="field" style="left:602px;top:182px;width:231px;height:54px">Full Name</div>
  <div class="field" style="left:852px;top:182px;width:231px;height:54px">email@example.com</div>
  <div class="label" style="left:602px;top:262px">MESSAGE</div>
  <div class="field" style="left:602px;top:286px;width:481px;height:104px">Your Message</div>
  <div class="btn" style="left:602px;top:420px;width:103px;height:36px">Send</div>

  <div class="abs" style="left:113px;top:492px;display:flex;align-items:center;gap:14px">
    <span style="width:42px;height:42px;border-radius:50%;background:var(--brand)"></span>
    <span style="font-size:38px;font-weight:600;color:#fff">Halvorn</span>
  </div>
  <div class="abs" style="left:113px;top:565px;width:330px;font-size:15px;line-height:1.45;color:#e4e4f2">Our consultancy was founded with the mission to enhance organizational safety performance through effective leadership. We believe that strong leadership</div>

  <div class="col-head" style="left:602px;top:505px">Quick Link</div>
  <div class="col-head" style="left:762px;top:505px">Resources</div>
  <div class="col-head" style="left:910px;top:505px">Our Services</div>
  <div class="col" style="left:602px;top:540px">Home<br>About Us<br>Our Vision<br>Success Stories</div>
  <div class="col" style="left:762px;top:540px">Safety Report<br>Blogs<br>News Update<br>FAQ's</div>
  <div class="col" style="left:910px;top:540px">Leadership Training Programs<br>Safety Culture Assessment<br>Customized Safety Processes</div>
  <div class="abs" style="left:0;top:732px;width:1200px;text-align:center;font-size:12px;color:#c8c8de">© Copyright 2024 <b style="color:#fff">Halvorn Ventures International</b>. All Rights Reserved.</div>
</section>

</body>
</html>
```